seeking a modern Business Card design for Roof Plumbering Business

wexcombe roof plumbing is a local metal re-roof and new construction specialist. We are seeking a modern business card to assist with networking within the industry. Our services are predominantly the installation of metal roofs on new houses, however we also do re-roofs when an existing roof needs replacing. We service both residential and commercial properties. Please include the below details on the card:
Name: Owen Wexcombe
Phone: 0471 385 962
Email: owenwexcomberoofing@mailnest.example

Residential & Commercial
Re-roof & New Construction
Fully Insured

I have uploaded our business logo, which we think would suit a black background. Please use all lower case for business name.
Cheers
Updates

Hey Guys, As requested I've uploaded a Pdf version of my logo. Hopefully this help. Thanks

Industry/Entity Type

Business

Contact Information for Business Card

Name: Owen Wexcombe
Phone: 0471 385 962

Residential & Commercial
Fully Insured

Font styles to use
Serif
Sans Serif

Requirements
Must have
• Name must be all lower case "wexcombe roof plumbing"
Nice to have
• Stick with Logo Colours

```html
<!DOCTYPE html>
<html lang="en">
<head>
<meta charset="utf-8">
<title>wexcombe roof plumbing – business card</title>
<link rel="stylesheet" href="https://fonts.googleapis.com/css2?family=Figtree:wght@400;700&display=swap">
<style>
  :root {
    --backdrop: #939393;
    --card-black: #1f1f1f;
    --brand-blue: #36a0d4;
    --rule-white: #ffffff;
    --text-light: #ffffff;
    --text-dark: #1c1c1c;
  }
  * { margin: 0; padding: 0; box-sizing: border-box; }
  html, body {
    width: 1200px;
    height: 1200px;
    overflow: hidden;
    background: var(--backdrop);
    font-family: "Figtree", sans-serif;
  }
  .business-card {
    position: absolute;
    left: 0;
    top: 266px;
    width: 1200px;
    height: 667px;
    background: var(--card-black);
  }
  .brand-name {
    position: absolute;
    left: 124px;
    top: 212px;
    width: 390px;
    font-size: 54px;
    line-height: 1.05;
    font-weight: 400;
    color: var(--brand-blue);
    letter-spacing: 0.5px;
  }
  .contact-block {
    position: absolute;
    left: 623px;
    top: 264px;
    color: var(--text-light);
  }
  .contact-name {
    font-size: 36px;
    font-weight: 700;
    line-height: 1;
    margin-bottom: 22px;
  }
  .contact-line {
    display: flex;
    align-items: center;
    font-size: 25px;
    line-height: 1;
    height: 39px;
  }
  .contact-icon {
    width: 28px;
    height: 22px;
    margin-right: 24px;
    flex: none;
  }
  .white-rule {
    position: absolute;
    left: 0;
    top: 558px;
    width: 100%;
    height: 8px;
    background: var(--rule-white);
  }
  .service-band {
    position: absolute;
    left: 0;
    top: 566px;
    width: 100%;
    height: 69px;
    background: var(--brand-blue);
    color: var(--text-dark);
    font-size: 25px;
  }
  .service-item {
    position: absolute;
    top: 50%;
    transform: translateY(-50%);
    white-space: nowrap;
  }
</style>
</head>
<body>
  <div class="business-card">
    <div class="brand-name">wexcombe roof plumbing</div>

    <div class="contact-block">
      <div class="contact-name">Owen Wexcombe</div>
      <div class="contact-line">
        <svg class="contact-icon" viewBox="0 0 28 22" aria-hidden="true">
          <path d="M2 8 C2 3 26 3 26 8 L26 10 L20 10 L20 7 C17 6 11 6 8 7 L8 10 L2 10 Z" fill="var(--brand-blue)"/>
          <path d="M7 12 L21 12 L24 20 L4 20 Z" fill="var(--brand-blue)"/>
          <circle cx="14" cy="15.5" r="2.6" fill="var(--card-black)"/>
        </svg>
        <span>0471 385 962</span>
      </div>
      <div class="contact-line">
        <svg class="contact-icon" viewBox="0 0 28 22" aria-hidden="true">
          <rect x="2" y="3" width="24" height="16" fill="none" stroke="var(--brand-blue)" stroke-width="2.2"/>
          <path d="M2 3 L14 12 L26 3 M2 19 L11 10 M26 19 L17 10" fill="none" stroke="var(--brand-blue)" stroke-width="2"/>
        </svg>
        <span>owenwexcomberoofing@mailnest.example</span>
      </div>
    </div>

    <div class="white-rule"></div>
    <div class="service-band">
      <span class="service-item" style="left:115px">Residential &amp; Commercial</span>
      <span class="service-item" style="left:463px">-</span>
      <span class="service-item" style="left:501px">Re-roof &amp; New Construction</span>
      <span class="service-item" style="left:890px">-</span>
      <span class="service-item" style="left:928px">Fully Insured</span>
    </div>
  </div>
</body>
</html>
```